Castellano Wine label**

Hi, we need a design for a white, red and sparkling wine label. We are a small italian restaurant (Castellano) and we want to release some wines under our personal brand. The restaurant has a rustic, italian provance style with with a slight modern, clean lines look. We would like a design that represent our mission to provide as authentic Italian food as we can, something that feels that it has been brought from the heart of Italy.
https://www.castellanotrattoria.ru/

```html
<!DOCTYPE html>
<html lang="en">
<head>
<meta charset="utf-8">
<title>Castellano Wine Labels</title>
<link href="https://fonts.googleapis.com/css2?family=Delius&family=Great+Vibes&family=Oswald:wght@300;400&family=Playfair+Display:ital@0;1&display=swap" rel="stylesheet">
<style>
  :root {
    --page: #ffffff;
    --cream: #f6efe2;
    --sand: #e3dfc0;
    --paper: #f7f6f2;
    --ink: #2b2826;
    --teal: #2f9a9c;
    --wine: #8e2a4f;
    --plum: #b0306f;
    --gold-a: #b98b3c;
    --gold-b: #f4dc8a;
    --monogram: #e6dcbf;
    --s1: #6fc7c9; --s2: #c83a7a; --s3: #e6c24a; --s4: #8cbf4a; --s5: #7b3b8c; --s6: #e56b3c;
  }
  * { margin: 0; padding: 0; box-sizing: border-box; }
  html, body { width: 1200px; height: 1007px; overflow: hidden; background: var(--page); }
  .canvas { position: relative; width: 1200px; height: 1007px; }

  .label { position: absolute; width: 242px; height: 538px; overflow: hidden; }
  .label--landscape { left: 114px; top: 277px; background: var(--cream); }
  .label--festive { left: 513px; top: 285px; background: var(--sand); }
  .label--paper { left: 889px; top: 286px; background: var(--paper); }

  .gold-rule { position: absolute; left: 0; width: 100%; height: 6px;
    background: linear-gradient(90deg, var(--gold-a), var(--gold-b) 45%, var(--gold-a) 75%, var(--gold-b)); }

  .stripe-band { position: absolute; left: 0; width: 100%; height: 9px;
    background: repeating-linear-gradient(90deg,
      var(--s1) 0 12px, var(--s2) 12px 20px, var(--s3) 20px 26px, var(--s1) 26px 34px,
      var(--s4) 34px 40px, var(--s5) 40px 48px, var(--s2) 48px 58px, var(--s6) 58px 64px); }

  .wordmark { position: absolute; left: 0; width: 100%; text-align: center;
    font-family: "Delius", cursive; font-size: 30px; letter-spacing: 6px; color: var(--ink); }

  .artwork { position: absolute; }
  .artwork--fields { left: 0; top: 91px; width: 100%; height: 106px;
    background: linear-gradient(180deg, #d9d9d9 0%, #8e8e8e 35%, #5a5a5a 55%, #3a3a3a 100%); }
  .artwork--monogram { left: 46px; top: 228px; width: 170px; height: 120px;
    background: radial-gradient(ellipse at center, var(--monogram) 0%, var(--cream) 75%); }
  .artwork--crowd { left: 0; top: 156px; width: 100%; height: 259px;
    background: linear-gradient(135deg, #e0357a, #c21f4b 40%, #8a3aa0 75%, #f0a0b8); }
  .artwork--band { left: 12px; top: 208px; width: 222px; height: 228px; border-radius: 8px;
    background: linear-gradient(135deg, #e6447f, #c42a4f 45%, #8b3b9c 80%, #f2b0c0); }

  .tagline-caps { position: absolute; left: 0; width: 100%; text-align: center;
    font-family: "Playfair Display", serif; font-size: 21px; letter-spacing: 1.5px; color: var(--teal); }
  .tagline-italic { position: absolute; left: 0; width: 100%; text-align: center;
    font-family: "Playfair Display", serif; font-style: italic; color: var(--wine); }
  .tagline-script { position: absolute; left: 0; width: 100%; text-align: center;
    font-family: "Great Vibes", cursive; color: var(--wine); }
  .tagline-condensed { position: absolute; left: 0; width: 100%; text-align: center;
    font-family: "Oswald", sans-serif; }
</style>
</head>
<body>
<main class="canvas">

  <section class="label label--landscape">
    <div class="gold-rule" style="top:84px"></div>
    <div class="artwork artwork--fields" role="img" aria-label="Black and white photograph of vineyard rows before snowy mountains"></div>
    <div class="gold-rule" style="top:196px"></div>
    <div class="artwork artwork--monogram" role="img" aria-label="Faint decorative monogram area"></div>
    <div class="wordmark" style="top:364px">castellano</div>
    <div class="stripe-band" style="top:408px"></div>
    <div class="tagline-caps" style="top:443px">ITALIAN FINE</div>
    <div class="tagline-italic" style="top:462px; font-size:32px">wine</div>
  </section>

  <section class="label label--festive">
    <div class="wordmark" style="top:93px">castellano</div>
    <div class="stripe-band" style="top:133px"></div>
    <div class="gold-rule" style="top:149px"></div>
    <div class="artwork artwork--crowd" role="img" aria-label="Colourful cubist illustration of musicians and guests with wine glasses"></div>
    <div class="gold-rule" style="top:413px"></div>
    <div class="tagline-script" style="top:430px; font-size:33px">Italian Fine</div>
    <div class="tagline-condensed" style="top:468px; font-size:38px; font-weight:400; color:var(--plum)">wine</div>
  </section>

  <section class="label label--paper">
    <div class="wordmark" style="top:92px">castellano</div>
    <div class="stripe-band" style="top:132px"></div>
    <div class="gold-rule" style="top:148px"></div>
    <div class="artwork artwork--band" role="img" aria-label="Colourful cubist illustration of a guitarist and friends raising wine glasses"></div>
    <div class="tagline-condensed" style="top:474px; font-size:36px; font-weight:300; color:var(--teal)">Italian Wine</div>
  </section>

</main>
</body>
</html>
```